3 x Webpage Homepage Banner for New Scrap Metal Company website

New website (currently under construction) for a scrap metal recycling company require 3 home page banner that give visitor have a sense of confident and relevance in the company. Feeling good about the products and value.

I have attached here a file name "website home page" to show the currently general idea of the design of the webpage. Two more file "Regular Login 1" and "Regular Login 2" to show the currently "looks" when a user visit the page. The current banner is a dummy.

One of the file titled "Company Image" is the picture of our company which I would also like to have it in one of the banner.

```html
<!DOCTYPE html>
<html lang="en">
<head>
<meta charset="UTF-8">
<title>Recycling Industrial Metal Scraps – Banner</title>
<link rel="stylesheet" href="https://fonts.googleapis.com/css2?family=Jost:wght@400;500;600;700&display=swap">
<style>
  :root {
    --sky-top: #c9d3df;
    --sky-low: #e3e6ea;
    --scrap-dark: #3b3127;
    --scrap-mid: #6b5a46;
    --gold: #c9a24a;
    --gold-deep: #b08a3c;
    --brown-dark: #3d3220;
    --white: #ffffff;
    --black: #000000;
  }
  * { margin: 0; padding: 0; box-sizing: border-box; }
  html, body {
    width: 1200px; height: 549px; overflow: hidden;
    background: var(--white);
  }
  .banner {
    position: relative;
    width: 1200px; height: 549px;
    overflow: hidden;
    font-family: "Jost", sans-serif;
    color: var(--white);
  }
  .banner__photo {
    position: absolute; inset: 0;
    background:
      linear-gradient(180deg, rgba(0,0,0,0) 0%, rgba(0,0,0,0) 55%, var(--scrap-mid) 70%, var(--scrap-dark) 100%),
      linear-gradient(180deg, var(--sky-top) 0%, var(--sky-low) 60%);
  }
  .banner__overlay {
    position: absolute; inset: 0;
    width: 1200px; height: 549px;
  }
  .banner__content {
    position: absolute;
    left: 54px; top: 158px;
  }
  .banner__kicker {
    font-size: 30px;
    font-weight: 500;
    letter-spacing: 5.2px;
    line-height: 1;
  }
  .banner__title {
    margin-top: 10px;
    font-size: 57px;
    font-weight: 700;
    letter-spacing: 1px;
    line-height: 1;
  }
  .banner__features {
    list-style: none;
    margin-top: 22px;
  }
  .banner__feature {
    display: flex; align-items: center;
    height: 32px;
    font-size: 13px;
    font-weight: 400;
  }
  .banner__feature svg {
    width: 20px; height: 20px; margin-right: 7px; flex: none;
  }
  .banner__button {
    display: inline-flex; align-items: center; justify-content: center;
    margin-top: 22px;
    width: 165px; height: 44px;
    background: var(--black);
    color: var(--white);
    font-size: 13px; font-weight: 600;
    letter-spacing: 1.6px;
    text-decoration: none;
    border-radius: 2px;
  }
</style>
</head>
<body>
<section class="banner">
  <div class="banner__photo" role="img" aria-label="Photo of a blue crane grapple lifting scrap metal over large heaps in a recycling yard under a cloudy sky"></div>

  <svg class="banner__overlay" viewBox="0 0 1200 549" aria-hidden="true">
    <defs>
      <linearGradient id="goldFade" x1="0" y1="0" x2="1" y2="0">
        <stop offset="0" stop-color="var(--brown-dark)" stop-opacity="0.92"/>
        <stop offset="0.45" stop-color="var(--gold-deep)" stop-opacity="0.88"/>
        <stop offset="1" stop-color="var(--gold)" stop-opacity="0.9"/>
      </linearGradient>
    </defs>
    <polygon points="0,0 407,0 632,278 414,549 0,549" fill="url(#goldFade)"/>
  </svg>

  <div class="banner__content">
    <p class="banner__kicker">RECYCLING INDUSTRIAL</p>
    <h1 class="banner__title">METAL SCRAPS</h1>
    <ul class="banner__features">
      <li class="banner__feature">
        <svg viewBox="0 0 20 20"><circle cx="10" cy="10" r="8.8" fill="none" stroke="#fff" stroke-width="1.4"/><path d="M6.2 10.2l2.6 2.6 5-5.2" fill="none" stroke="#fff" stroke-width="1.5" stroke-linecap="round" stroke-linejoin="round"/></svg>
        Lorem ipsum dolor sit amet, consectetur
      </li>
      <li class="banner__feature">
        <svg viewBox="0 0 20 20"><circle cx="10" cy="10" r="8.8" fill="none" stroke="#fff" stroke-width="1.4"/><path d="M6.2 10.2l2.6 2.6 5-5.2" fill="none" stroke="#fff" stroke-width="1.5" stroke-linecap="round" stroke-linejoin="round"/></svg>
        Adipiscing elit, sed do eiusmod tempor incididunt
      </li>
      <li class="banner__feature">
        <svg viewBox="0 0 20 20"><circle cx="10" cy="10" r="8.8" fill="none" stroke="#fff" stroke-width="1.4"/><path d="M6.2 10.2l2.6 2.6 5-5.2" fill="none" stroke="#fff" stroke-width="1.5" stroke-linecap="round" stroke-linejoin="round"/></svg>
        Pt labore et dolore magna aliqua.
      </li>
    </ul>
    <a class="banner__button" href="#services">OUR SERVICES</a>
  </div>
</section>
</body>
</html>
```